Fitness business need 3x3 card to promote 6wk boot camp nutrition challenge

Hi, we're looking for someone to make our current card look better and more modern. We want to keep the text the same, but we want a better design. We also want to keep the woman on the front of the card. The card is for both men and women so we want it to feel inclusive and bright. The idea is to make the card look more modern. We want some pops of color. The main feature is to promote the pricing on the back of the card. It would be nice if that continues to look like a coupon or if it stands out with a bright color or background.

Target Market(s)

Men and women looking to get in shape

Industry/Entity Type

Fitness

Font styles to use
Serif
Sans Serif

Colors
3176b5
0255a3
33a6d7
f37122
ec1f27

Requirements
Must have
• front and back, use pic of women provided

```html
<!DOCTYPE html>
<html lang="en">
<head>
<meta charset="utf-8">
<title>Boot Camp 6 Week Challenge Card</title>
<link rel="stylesheet" href="https://fonts.googleapis.com/css2?family=Bowlby+One+SC&family=Oswald:wght@500;600&family=Open+Sans:ital,wght@0,600;0,700;0,800;1,700&display=swap">
<style>
:root{
  --blue:#3176b5;
  --navy:#0255a3;
  --sky:#33a6d7;
  --orange:#f37122;
  --red:#ec1f27;
  --deep-red:#b5121b;
  --ink:#1a1a1a;
  --paper:#ffffff;
  --stage:#e8e8e8;
  --gold:#f6c453;
}
*{box-sizing:border-box;margin:0;padding:0}
html,body{width:1200px;height:900px;overflow:hidden;background:var(--stage)}
body{position:relative;font-family:"Open Sans",sans-serif}
.card{position:absolute;top:180px;width:540px;height:540px;overflow:hidden;box-shadow:0 10px 30px rgba(0,0,0,.18)}
.card--back{left:40px;background:var(--paper)}
.card--front{left:620px;background:var(--sky)}

/* back card */
.brush-band{position:absolute;left:0;top:150px;width:540px;height:280px}
.back-title{position:absolute;left:36px;top:36px;font-family:"Bowlby One SC",sans-serif;font-size:64px;color:var(--red);line-height:1;letter-spacing:1px;white-space:nowrap}
.back-subtitle{position:absolute;left:40px;top:108px;font-weight:800;font-size:25px;color:var(--navy);letter-spacing:-.3px;white-space:nowrap}
.back-dates{position:absolute;left:40px;top:142px;font-weight:600;font-size:18px;color:var(--ink);white-space:nowrap}
.weights-ribbon{position:absolute;left:0;top:192px;width:510px;height:46px;background:var(--orange);display:flex;align-items:center;padding-left:28px;font-weight:800;font-size:24px;line-height:1;color:var(--paper);letter-spacing:.3px;white-space:nowrap;clip-path:polygon(0 0,100% 0,96% 100%,0 100%)}
.back-copy{position:absolute;left:34px;top:250px;color:var(--paper)}
.back-copy .lead{font-weight:800;font-size:21px;margin-bottom:4px;white-space:nowrap}
.back-copy li{list-style:none;font-weight:700;font-size:15px;line-height:1.45;padding-left:16px;position:relative;white-space:nowrap}
.back-copy li::before{content:"";position:absolute;left:0;top:6px;border-left:9px solid var(--orange);border-top:5px solid transparent;border-bottom:5px solid transparent}
.back-copy .cta{margin-top:6px;font-style:italic;font-weight:700;font-size:21px;color:var(--gold)}
.coupon{position:absolute;left:226px;top:350px;width:296px;height:92px;background:var(--paper);border:2px dashed var(--red);display:flex;align-items:center;padding:0 12px;white-space:nowrap}
.coupon .count{font-family:"Oswald",sans-serif;font-weight:600;font-size:72px;line-height:1;color:var(--ink)}
.coupon .label{font-family:"Oswald",sans-serif;font-weight:600;font-size:24px;line-height:.95;color:var(--ink);margin:0 8px 0 6px}
.coupon .price{font-family:"Oswald",sans-serif;font-weight:600;font-size:58px;line-height:1;color:var(--red)}
.coupon .price sup{font-size:24px}
.contact{position:absolute;right:22px;top:456px;text-align:right;color:var(--ink)}
.contact .phone{font-weight:800;font-size:20px;white-space:nowrap}
.contact .address{font-weight:600;font-size:14px;line-height:1.3}
.learn{position:absolute;left:34px;top:452px;color:var(--ink)}
.learn .intro{font-style:italic;font-weight:700;font-size:14px;color:var(--blue)}
.learn .url{font-weight:700;font-size:17px}
.learn .social{margin-top:6px;display:flex;align-items:center;gap:8px;font-weight:700;font-size:15px}
.learn .social .dot{width:14px;height:14px;border-radius:50%;background:var(--ink)}

/* front card */
.front-bg{position:absolute;inset:0}
.athlete-photo{position:absolute;left:220px;top:60px;width:320px;height:400px}
.title-band{position:absolute;left:0;top:40px;width:440px;height:120px;background:var(--deep-red);clip-path:polygon(0 12%,100% 0,100% 88%,0 100%)}
.front-title{position:absolute;left:32px;top:58px;font-family:"Bowlby One SC",sans-serif;font-size:50px;color:var(--paper);line-height:1;white-space:nowrap}
.front-dates{position:absolute;left:36px;top:118px;font-family:"Oswald",sans-serif;font-weight:500;font-size:19px;color:var(--paper);white-space:nowrap}
.challenge-ribbon{position:absolute;left:80px;top:172px;width:400px;height:80px;background:var(--red);display:flex;align-items:center;padding-left:20px;color:var(--paper);white-space:nowrap;clip-path:polygon(0 8%,100% 0,100% 92%,0 100%)}
.challenge-ribbon .num{font-family:"Oswald",sans-serif;font-weight:600;font-size:64px;line-height:1;margin-right:10px}
.challenge-ribbon .words{font-weight:800;font-size:24px;line-height:1.05}
.challenge-ribbon .words small{display:block;font-size:19px}
.url-ribbon{position:absolute;left:90px;top:440px;width:420px;height:36px;background:var(--navy);display:flex;align-items:center;justify-content:center;color:var(--paper);font-weight:600;font-size:15px;white-space:nowrap;clip-path:polygon(0 0,96% 0,100% 50%,96% 100%,0 100%)}
</style>
</head>
<body>

<section class="card card--back" aria-label="Back of card">
  <svg class="brush-band" viewBox="0 0 540 280" aria-hidden="true">
    <path d="M0 30 Q120 10 260 25 T540 5 L540 250 Q400 275 260 255 T0 270 Z" fill="#0255a3"/>
    <path d="M0 60 Q200 40 540 30 L540 120 Q300 150 0 140 Z" fill="#3176b5" opacity=".55"/>
  </svg>
  <h1 class="back-title">BOOT CAMP</h1>
  <p class="back-subtitle">6 Week Fitness &amp; Nutrition Challenge</p>
  <p class="back-dates">October 2nd to November 11th</p>
  <div class="weights-ribbon">NO BARBELLS! NO HEAVY WEIGHTS</div>
  <div class="back-copy">
    <p class="lead">BURN FAT, BUILD MUSCLE &amp; HAVE FUN!</p>
    <ul>
      <li>Tons of classes led by world-class coaches.</li>
      <li>Personalized nutrition planning, prizes, and more!</li>
    </ul>
    <p class="cta">Sign up Today!</p>
  </div>
  <div class="coupon">
    <span class="count">6</span>
    <span class="label">WEEKS<br>FOR ONLY</span>
    <span class="price">249<sup>$</sup></span>
  </div>
  <div class="contact">
    <p class="phone">Call: (555) 014-2287</p>
    <p class="address">42 Harbor Lane, Millbrook,<br>NY 10003</p>
  </div>
  <div class="learn">
    <p class="intro">Learn more at:</p>
    <p class="url">www.ironpeakfit.com</p>
    <p class="social"><span class="dot"></span>@ironpeakfit</p>
  </div>
</section>

<section class="card card--front" aria-label="Front of card">
  <svg class="front-bg" viewBox="0 0 540 540" aria-hidden="true">
    <rect width="540" height="540" fill="#33a6d7"/>
    <path d="M200 0 H540 V480 Q420 500 300 460 Z" fill="#f37122" opacity=".85"/>
    <path d="M0 300 Q150 260 300 330 T540 320 V540 H0 Z" fill="#0255a3" opacity=".35"/>
  </svg>
  <svg class="athlete-photo" viewBox="0 0 320 400" role="img" aria-label="Black and white photo of a woman athlete seated with a medicine ball">
    <defs>
      <linearGradient id="photoTone" x1="0" y1="0" x2="1" y2="1">
        <stop offset="0" stop-color="#9a9a9a"/>
        <stop offset="1" stop-color="#2e2e2e"/>
      </linearGradient>
    </defs>
    <rect width="320" height="400" rx="6" fill="url(#photoTone)" opacity=".9"/>
  </svg>
  <div class="title-band"></div>
  <h2 class="front-title">BOOT CAMP</h2>
  <p class="front-dates">October 2nd to November 11th</p>
  <div class="challenge-ribbon">
    <span class="num">6</span>
    <span class="words">Week Fitness &amp;<small>Nutrition Challenge</small></span>
  </div>
  <div class="url-ribbon">www.ironpeakfit.com/bootcamp</div>
</section>

</body>
</html>
```